One page financial canvas needed

I am in the process of developing a financial planning process that uses a one page canvas as a tool for financial education and to explain simple and complex financial strategies to clients. I have the layout and content sorted, just need a hand making it look professional.

It should be a fairly simple project and i have attached a very rough hand drawn canvas showing the desired layout and content. Please feel free to be creative with the design keeping in mind this layout has been chosen to achieve certain outcomes.

Target Market(s)

25-45 Year old Homeowners who are interested in taking better care of the finances

Industry/Entity Type

Financial

Colors

Designer to choose colors to be used in the design.

Requirements
Must have
• very close to the layout in the attached file

```html
<!DOCTYPE html>
<html lang="en">
<head>
<meta charset="utf-8">
<title>Financial Planning Process</title>
<link rel="stylesheet" href="https://fonts.googleapis.com/css2?family=Source+Sans+3:wght@400;600&display=swap">
<style>
  :root {
    --burgundy: #9b1b35;
    --ink: #111111;
    --paper: #ffffff;
    --bubble: #bdbec0;
    --bubble-edge: #9fa0a3;
    --bar: #b9babc;
    --tab: #e9e9ea;
    --text: #1d1d1f;
    --skyline: rgba(155, 27, 53, 0.10);
  }
  * { box-sizing: border-box; margin: 0; padding: 0; }
  html, body { width: 1200px; height: 927px; overflow: hidden; background: var(--paper); }
  body { font-family: "Source Sans 3", "Myriad Pro", Arial, sans-serif; color: var(--text); }

  .canvas { position: relative; width: 1200px; height: 927px; }

  .board {
    position: absolute; left: 0; top: 0; width: 1200px; height: 765px;
    background: var(--burgundy); overflow: hidden;
  }

  .decor { position: absolute; left: 0; top: 0; width: 1200px; height: 765px; }

  .title {
    position: absolute; left: 197px; top: 45px; width: 818px; height: 88px;
    display: flex; align-items: center; justify-content: center;
    color: var(--paper); font-size: 60px; font-weight: 400; letter-spacing: 0.5px;
  }

  .box {
    position: absolute; background: var(--paper); overflow: hidden;
  }
  .box__label {
    position: relative; z-index: 1;
    display: block; padding: 10px 0 0 15px;
    font-size: 24px; font-weight: 400; color: var(--text);
  }
  .box__skyline {
    position: absolute; left: 0; right: 0; bottom: 0; height: 62%;
    background: linear-gradient(to bottom, rgba(155,27,53,0) 0%, var(--skyline) 35%, var(--skyline) 100%);
  }

  .box--goals        { left: 45px;  top: 201px; width: 240px; height: 547px; }
  .box--income       { left: 333px; top: 201px; width: 240px; height: 263px; }
  .box--income .box__label, .box--expenses .box__label { padding-left: 30px; }
  .box--expenses     { left: 644px; top: 201px; width: 238px; height: 263px; }
  .box--assets       { left: 333px; top: 488px; width: 240px; height: 260px; }
  .box--debt         { left: 644px; top: 488px; width: 238px; height: 260px; }
  .box--debt .box__label { padding-left: 52px; }
  .box--fears        { left: 924px; top: 201px; width: 240px; height: 172px; }
  .box--frustrations { left: 924px; top: 403px; width: 240px; height: 174px; }
  .box--partners     { left: 924px; top: 604px; width: 240px; height: 144px; }

  .node {
    position: absolute; display: flex; align-items: center; justify-content: center;
    background: var(--bubble); border: 2px solid var(--bubble-edge); border-radius: 50%;
    font-size: 24px; color: var(--text);
  }
  .node--cash-flow { left: 539px; top: 444px; width: 146px; height: 66px; }
  .node--wealth    { left: 533px; top: 709px; width: 158px; height: 66px; padding-bottom: 8px; }

  .timeline {
    position: absolute; left: 0; top: 791px; width: 1200px; height: 115px;
    background: var(--bar);
    border-top: 3px solid var(--paper); border-bottom: 3px solid var(--paper);
    box-shadow: 0 -2px 0 var(--bar), 0 2px 0 var(--bar);
  }
  .timeline__label {
    position: absolute; left: 0; top: 0; width: 194px; height: 109px;
    background: var(--tab);
    border: 3px solid var(--paper); border-left: none;
    border-radius: 0 56px 56px 0;
    display: flex; align-items: center; padding-left: 30px;
    font-size: 48px; color: var(--text);
  }
</style>
</head>
<body>
<main class="canvas">
  <section class="board">
    <svg class="decor" viewBox="0 0 1200 765" aria-hidden="true">
      <!-- ribbon tails -->
      <polygon points="152,61 235,61 235,159 180,159 205,110" fill="var(--ink)"/>
      <polygon points="977,61 1133,61 1105,105 1133,152 977,152" fill="var(--ink)"/>
      <!-- title band -->
      <polygon points="197,45 1015,45 990,133 222,133" fill="var(--ink)"/>
      <!-- connectors -->
      <g stroke="var(--paper)" stroke-width="4" stroke-dasharray="12 12" fill="none">
        <line x1="309" y1="235" x2="309" y2="655"/>
        <line x1="612" y1="245" x2="612" y2="440"/>
        <line x1="612" y1="515" x2="612" y2="712"/>
        <line x1="904" y1="228" x2="904" y2="668"/>
        <line x1="348" y1="476" x2="538" y2="476"/>
        <line x1="690" y1="476" x2="818" y2="476"/>
        <line x1="939" y1="389" x2="1150" y2="389"/>
        <line x1="962" y1="588" x2="1128" y2="588"/>
      </g>
    </svg>

    <h1 class="title">Financial Planning Process</h1>

    <div class="box box--goals"><span class="box__label">Goals:</span><div class="box__skyline" role="img" aria-label="Faint city skyline backdrop"></div></div>
    <div class="box box--income"><span class="box__label">Income:</span><div class="box__skyline" role="img" aria-label="Faint city skyline backdrop"></div></div>
    <div class="box box--expenses"><span class="box__label">Expenses:</span><div class="box__skyline" role="img" aria-label="Faint city skyline backdrop"></div></div>
    <div class="box box--assets"><span class="box__label">Assets:</span><div class="box__skyline" role="img" aria-label="Faint city skyline backdrop"></div></div>
    <div class="box box--debt"><span class="box__label">Debt:</span><div class="box__skyline" role="img" aria-label="Faint city skyline backdrop"></div></div>
    <div class="box box--fears"><span class="box__label">Fears:</span><div class="box__skyline" role="img" aria-label="Faint city skyline backdrop"></div></div>
    <div class="box box--frustrations"><span class="box__label">Frustrations:</span><div class="box__skyline" role="img" aria-label="Faint city skyline backdrop"></div></div>
    <div class="box box--partners"><span class="box__label">Partners:</span><div class="box__skyline" role="img" aria-label="Faint city skyline backdrop"></div></div>

    <div class="node node--cash-flow">Cash Flow</div>
    <div class="node node--wealth">Wealth</div>
  </section>

  <section class="timeline">
    <div class="timeline__label">Time:</div>
  </section>
</main>
</body>
</html>
```